Tarek & Lubna's 50th Anniversary Celebration & Reunion

I need a flyer to send out via email and for posting on chatterboard to invite guests to a 50th wedding anniversary / family reunion.

Location is sunny La Jolla CA the Pearl of San Diego's Shore.

Week long daily activities starting Mon July 28-Aug 1st Friday, The event will be on Wednesday.
* Daily Catered Family Breakfast at the Marlow Hall of La Jolla
* Daily group activities including
*Exploring La Jolla Beaches & Ocean Cave Kayaking
*TideRealm Private Behind the Scenes Tour
*World Famous Pellham Wildlife Park
*Sunset Balloon Ride
*Private Yatch on the Bay

Actual Anniversary event will take place Thursday December 28, 2013 at 5pm at the Marlow Hall.

There are many local hotels around the Marlow Hall. 4213 Brindle Ln, La Jolla, CA 92058

Host is Kamil and the entire Haddour Family. For questions, please email Kamil@thelinden-feasts.com

Target Market(s)

all ages from 10 year olds to 70 year olds. Should appeal to all

Industry/Entity Type

Wedding

Font styles to use
Script

Colors

Designer to choose colors to be used in the design.

Requirements
Must have
• Fun graphics, including one with a stretch limo as there will be one available

Photo enclosed
Nice to have
• Logo for TideRealm Inserting a picture of an actual wedding 50 years ago or so of the bride and groom. incorporating the limo cropped out of the picture attached would also be nice

```html
<!DOCTYPE html>
<html lang="en">
<head>
<meta charset="utf-8">
<title>Tarek &amp; Lubna – 50th Wedding Anniversary</title>
<link rel="stylesheet" href="https://fonts.googleapis.com/css2?family=Great+Vibes&family=Titillium+Web:wght@400;600&display=swap">
<style>
  :root {
    --backdrop: #e4e4e4;
    --paper: #f7f6f3;
    --paper-edge: #ecebe7;
    --sky-top: #bcdcd8;
    --sky-low: #e7efe9;
    --road: #dad8d2;
    --ink: #2f2a24;
    --gold: #a67a1c;
    --gold-light: #e0b84a;
    --gold-dark: #7a5510;
  }
  * { margin: 0; padding: 0; box-sizing: border-box; }
  html, body { width: 1200px; height: 900px; overflow: hidden; }
  body {
    background: var(--backdrop);
    font-family: "Titillium Web", sans-serif;
    display: flex; align-items: center; justify-content: center;
  }
  .flyer {
    position: relative;
    width: 664px; height: 868px;
    background: linear-gradient(180deg, var(--paper) 0%, var(--paper-edge) 100%);
    box-shadow: 0 6px 24px rgba(0,0,0,.18);
    overflow: hidden;
    text-align: center;
  }
  .scene-photo {
    position: absolute; left: 0; top: 0; width: 100%; height: 420px;
    background:
      linear-gradient(180deg, transparent 60%, var(--paper) 100%),
      linear-gradient(180deg, var(--sky-top) 0%, var(--sky-low) 34%, #6f8a58 42%, #2a2a2a 48%, #2a2a2a 62%, var(--road) 68%, var(--road) 100%);
  }
  .content { position: relative; padding-top: 38px; }
  .content p { line-height: 1.3; }
  .hosts-names {
    color: var(--gold); font-weight: 600; font-size: 22px; letter-spacing: 4px;
  }
  .invite-line {
    color: var(--ink); font-size: 35px; letter-spacing: 5px; margin-top: 0;
  }
  .invite-line, .content .invite-line { line-height: 1.1; }
  .gold-script {
    font-family: "Great Vibes", cursive;
    background: linear-gradient(180deg, var(--gold-light) 0%, var(--gold) 55%, var(--gold-dark) 100%);
    -webkit-background-clip: text; background-clip: text; color: transparent;
  }
  .year-mark { font-size: 136px; line-height: 1; margin-top: 200px; }
  .occasion { font-size: 78px; line-height: 1; margin-top: -16px; }
  .schedule { color: var(--ink); font-size: 19px; margin-top: 14px; }
  .content .event-lead { color: var(--gold); font-weight: 600; font-size: 24px; line-height: 1.15; margin-top: 2px; }
  .content .event-date { color: var(--gold); font-weight: 600; font-size: 26px; line-height: 1.15; }
  .event-date small { font-size: 14px; font-weight: 400; }
  .content .activities { color: var(--gold); font-size: 13px; line-height: 1.5; margin-top: 8px; padding: 0 30px; }
  .venue { color: var(--ink); font-size: 20px; margin-top: 10px; }
  .host-note { color: var(--gold); font-size: 17px; margin-top: 2px; }
  .contact { color: var(--ink); font-size: 17px; }
</style>
</head>
<body>
  <main class="flyer">
    <div class="scene-photo" role="img" aria-label="Black stretch limousine parked on a seaside road with palm trees under a clear sky"></div>
    <div class="content">
      <p class="hosts-names">TAREK &amp; LUBNA</p>
      <p class="invite-line">INVITING YOU FOR</p>
      <h1 class="gold-script year-mark">50th</h1>
      <h2 class="gold-script occasion">Wedding Anniversary</h2>
      <p class="schedule">Week long daily activities starting Mon July 28-Aug -1st Friday</p>
      <p class="event-lead">Actual Anniversary event will take place</p>
      <p class="event-date">Thursday December 28, 2013 <small>at 5pm at the Marlow Hall</small></p>
      <p class="activities">
        Daily Catered Family Breakfast | Daily group activities | Exploring La Jolla Beaches &amp; Ocean Cave Kayaking<br>
        TideRealm Private Behind the Scenes Tour | World Famous Pellham Wildlife Park | Sunset Balloon Ride<br>
        Private Yatch on the Bay
      </p>
      <p class="venue">
        AT THE MARLOW HALL OF LA JOLLA<br>
        There are many local hotels around the Marlow Hall.<br>
        4213 Brindle Ln, La Jolla, CA 92058
      </p>
      <p class="host-note">Host is Kamil and the entire Haddour Family</p>
      <p class="contact">For questions, please email Kamil@thelinden-feasts.com</p>
    </div>
  </main>
</body>
</html>
```